New and fresh Milk Bottle Label Design

We need 2 new Designs for our Milk Bottles (2.5% and 3,5% Milk) and are changing the label from Stretch Sleeves to Labels. The two different Milk have to be destincted easily by the customer. We are searching for a fresh design, which incorporates freshness, regionality, family enterprise and friendlyness.

Additionall Information here
http://brendlimilch.ch/
https://www.plaudernetz.ch/MolkereiBrendli/
Updates

Project Deadline Extended Reason: I need more options to choose, there are not enough Added Tuesday, April 4, 2017

Project Deadline Extended Reason: we have not found the design we want. it has to have the colour code and should not have too many elements. the cow should be brown Added Sunday, April 9, 2017

Target Market(s)

Eastern Switzerland (Regional)

Font styles to use
Sans Serif
Decorative

Requirements
Must have
• Image Language
• - Cows
• - the product itself in any variation
• - Milk glas, cup, etc.
• - Nature, naturally
• Elements Pastmilch:
• - verbrauchen bis: siehe oben (use until in German)
• - 1 L declaration
• - the Element Past
• - traditonally produced by family enterprise
• - Frische Vollmilch (German for fresh milk)
• - Vollmilch standardisiert 3.5% Fett, pasteurisiert, homogenisiert
• - Logo Brendli (fox) und Logo Gwerder
• - Logo Bodensee (lake)
• - Logo Tafelgut und below: heimat.siegel
• - Logo Terra Sigillum
• - EAN 13
• - Nährwerte: ca. pro 100 ml
• o Energie 270 kj / 65 kcal
• o Fett 3.5 g
•  davon gesättigte Fettsäuren 2.0 g
• o Kohlenhydrate 4.8 g
•  Davon Zucker 4.8 g
• o Ballaststoffe 0 g
• o Eiweiss 3.2 g
• o Salz 0.1 g
• - Molkerei Brendli, CH-9400 Rorschach, www.brendlimilch.ch
• - CH 5816 (in Oval, like on old packaging)
• - Vor Licht geschützt und bei max. +6°C aufbewahren
• - Recycling Logo PE
• Elemente Milchdrink:
• - verbrauchen bis: siehe oben
• - 1 L
• - Past
• - Frischer Milchdrink
• - Milch teilentrahmt 2.5%Fett, pasteurisiert, homogenisiert
• - Logo Brendli und Logo Gwerder
• - Logo Bodensee
• - Logo Tafelgut und darunter: heimat.siegel
• - Logo Terra Sigillum
• - EAN 13
• o Energie 230 kj / 55 kcal
• o Fett 2.5 g
•  davon gesättigte Fettsäuren 1.5 g
• o Kohlenhydrate 4.8 g
•  Davon Zucker 4.8 g
• o Ballaststoffe 0 g
• o Eiweiss 3.2 g
• o Salz 0.1 g
• - CH 5816 (in Oval)
• - Recycling Logo PE
Nice to have
• the colour red form our logo
Should not have
• too standard, the packaging everyone has...

```html
<!DOCTYPE html>
<html lang="de">
<head>
<meta charset="utf-8">
<title>Frische Vollmilch – Etikett</title>
<link href="https://fonts.googleapis.com/css2?family=Baloo+2:wght@700;800&family=Open+Sans:wght@600;700;800&display=swap" rel="stylesheet">
<style>
  :root {
    --sky-top: #3f86cf;
    --sky-low: #bcd7ee;
    --meadow: #7fae3a;
    --meadow-deep: #4f7f2a;
    --milk: #ffffff;
    --milk-shade: #e3e6ea;
    --brand-blue: #1c4fa8;
    --brand-blue-deep: #123a86;
    --brand-red: #e2242d;
    --lake-blue: #38b6e8;
    --cow-brown: #a65a2e;
    --cow-cream: #eee7d6;
  }
  html, body {
    margin: 0;
    padding: 0;
    width: 778px;
    height: 1200px;
    overflow: hidden;
    background: #ececec;
  }
  .label {
    position: relative;
    width: 778px;
    height: 1200px;
    overflow: hidden;
    font-family: "Open Sans", sans-serif;
  }
  .landscape {
    position: absolute;
    inset: 0;
    background:
      linear-gradient(180deg, var(--sky-top) 0%, #7fb2e2 18%, var(--sky-low) 34%, #9cb38a 44%, var(--meadow) 58%, var(--meadow-deep) 75%, var(--meadow) 100%);
  }
  .brand {
    position: absolute;
    left: 266px;
    width: 200px;
    top: 38px;
    text-align: center;
    color: var(--milk);
  }
  .brand-name {
    font-weight: 700;
    font-size: 28px;
    letter-spacing: 3px;
    text-transform: uppercase;
    line-height: 1;
  }
  .brand-region {
    font-weight: 700;
    font-size: 20px;
    margin-top: 22px;
  }
  .certificate {
    position: absolute;
    left: 628px;
    top: 84px;
    width: 98px;
    height: 146px;
    background: var(--milk);
    border-radius: 4px;
    box-shadow: 0 1px 4px rgba(0,0,0,.25);
  }
  .cow-emblem {
    position: absolute;
    left: 204px;
    top: 214px;
    width: 372px;
    height: 372px;
    border-radius: 50%;
    box-sizing: border-box;
    border: 16px solid rgba(255,255,255,.92);
    background:
      radial-gradient(circle at 42% 42%, rgba(238,231,214,.85) 0%, rgba(200,150,110,.65) 55%, rgba(166,90,46,.45) 100%);
    box-shadow: 0 0 0 6px rgba(255,255,255,.35);
  }
  .milk-wave {
    position: absolute;
    inset: 0;
  }
  .product-title {
    position: absolute;
    left: 0;
    top: 660px;
    width: 778px;
    height: 300px;
    margin: 0;
    font-family: "Baloo 2", sans-serif;
    font-weight: 800;
    color: var(--brand-blue);
    text-align: center;
  }
  .title-line-1 {
    position: absolute;
    left: 190px;
    width: 400px;
    top: 0;
    font-size: 96px;
    line-height: 1;
    transform: rotate(-3deg);
    -webkit-text-stroke: 3px var(--milk);
    paint-order: stroke fill;
  }
  .title-oval {
    position: absolute;
    left: 140px;
    top: 98px;
    width: 518px;
    height: 148px;
    border-radius: 50%;
    background: var(--brand-blue);
    transform: rotate(-6deg);
    border: 4px solid var(--milk);
    box-sizing: border-box;
  }
  .title-line-2 {
    position: absolute;
    left: 140px;
    width: 518px;
    top: 100px;
    font-size: 100px;
    line-height: 1;
    color: var(--milk);
    transform: rotate(-6deg);
    -webkit-text-stroke: 2px var(--brand-blue-deep);
    paint-order: stroke fill;
  }
  .past-tag {
    position: absolute;
    left: 384px;
    top: 890px;
    width: 246px;
    height: 64px;
    border-radius: 32px;
    background: var(--brand-red);
    border: 3px solid var(--milk);
    box-sizing: border-box;
    color: var(--milk);
    font-family: "Baloo 2", sans-serif;
    font-weight: 700;
    font-size: 42px;
    line-height: 62px;
    text-align: center;
    transform: rotate(-6deg);
  }
  .volume {
    position: absolute;
    left: 84px;
    top: 1052px;
    display: flex;
    align-items: flex-end;
    color: var(--brand-red);
  }
  .volume-number {
    font-weight: 800;
    font-size: 100px;
    line-height: .82;
  }
  .volume-unit {
    font-weight: 700;
    font-size: 28px;
    writing-mode: vertical-rl;
    transform: rotate(180deg);
    margin-left: 4px;
    line-height: 1;
  }
  .region-map {
    position: absolute;
    left: 390px;
    top: 1000px;
    width: 300px;
    height: 80px;
    border-radius: 45% 55% 40% 60%;
    background: var(--lake-blue);
    transform: rotate(-8deg);
  }
  .region-claim {
    position: absolute;
    left: 440px;
    top: 1080px;
    margin: 0;
    color: var(--brand-red);
    font-weight: 700;
    font-size: 24px;
    line-height: 1.2;
    transform: rotate(-8deg);
    transform-origin: left top;
    -webkit-text-stroke: 4px var(--milk);
    paint-order: stroke fill;
  }
  .region-flag {
    position: absolute;
    left: 666px;
    top: 1098px;
    width: 50px;
    height: 46px;
    background: var(--brand-red);
    border-radius: 3px;
  }
</style>
</head>
<body>
  <main class="label">
    <div class="landscape" role="img" aria-label="Photo of an alpine landscape: green meadows, a village and rocky peaks under a blue sky"></div>

    <header class="brand">
      <div class="brand-name">Tafelgut</div>
      <div class="brand-region">Ostschweiz</div>
    </header>

    <div class="certificate" role="img" aria-label="Terra Sigillum certificate badge"></div>

    <div class="cow-emblem" role="img" aria-label="Illustration of a brown and white cow framed by a swirl of milk"></div>

    <svg class="milk-wave" width="778" height="1200" viewBox="0 0 778 1200" aria-hidden="true">
      <defs>
        <linearGradient id="milkFill" x1="0" y1="0" x2="0" y2="1">
          <stop offset="0" stop-color="#ffffff"/>
          <stop offset="1" stop-color="#eef0f2"/>
        </linearGradient>
      </defs>
      <path d="M0 950 C120 910 260 930 380 965 C500 1000 600 985 660 925 C700 875 700 810 670 740 C720 760 760 800 778 830 L778 1200 L0 1200 Z" fill="url(#milkFill)"/>
      <path d="M0 995 C160 955 300 995 420 1025" fill="none" stroke="var(--milk-shade)" stroke-width="6"/>
    </svg>

    <h1 class="product-title">
      <span class="title-line-1">Frische</span>
      <span class="title-oval"></span>
      <span class="title-line-2">Vollmilch</span>
    </h1>

    <div class="past-tag">Past</div>

    <div class="volume">
      <span class="volume-number">1</span>
      <span class="volume-unit">Liter</span>
    </div>

    <div class="region-map" role="img" aria-label="Map outline of Lake Constance"></div>
    <p class="region-claim">Frische Milchprodukte<br>aus der Region</p>
    <div class="region-flag"></div>
  </main>
</body>
</html>
```